Esthetically Pleasing Core Values and Brand Promise for Accounting Firm

I would like a cohesive design that ties together my core values and brand promise. My firm, Maple Finch Advisory, provides accounting work to small businesses. I prefer modern and clean designs. I want my Core Values and Brand Promise to represent me - sole entrepreneur, married, mother of two kids, modern esthetics, clean lines, organized, colorful (teals, greys, white, yellows)

Industry/Entity Type

Public Accounting

Colors
33b8a4

```html
<!DOCTYPE html>
<html lang="en">
<head>
<meta charset="utf-8">
<title>Maple Finch Advisory – Core Values &amp; Brand Promise</title>
<link rel="stylesheet" href="https://fonts.googleapis.com/css2?family=Fira+Sans:wght@400;500&family=Poppins:wght@300;400;500;600&display=swap">
<style>
  :root{
    --stage:#434346;
    --teal:#4aaea9;
    --teal-brand:#33b8a4;
    --teal-light:#86d3cf;
    --teal-mid:#5bb7b2;
    --teal-deep:#1f6066;
    --yellow:#f3e97a;
    --yellow-ring:#f2e46a;
    --bullet:#d9cc3a;
    --white:#ffffff;
    --paper-top:#fbfbfb;
    --paper-bottom:#dadada;
    --ink:#3d3d3d;
  }
  *{box-sizing:border-box;margin:0;padding:0}
  html,body{width:1200px;height:1200px;overflow:hidden;background:var(--stage)}
  body{position:relative;font-family:"Fira Sans",Arial,sans-serif}

  .poster{
    position:absolute;left:204px;top:74px;width:822px;height:1066px;overflow:hidden;
    background:linear-gradient(180deg,var(--paper-top) 0%,#f0f0f0 55%,var(--paper-bottom) 100%);
  }
  .band{position:absolute;left:0;width:100%;background:var(--teal)}
  .band--top{top:0;height:22px}
  .band--bottom{bottom:0;height:16px}

  .graphic{position:absolute;left:0;top:0;width:1200px;height:1200px}

  .brand{position:absolute;left:415px;width:400px;text-align:center;color:var(--teal);font-family:"Poppins",Arial,sans-serif}
  .brand__line{position:absolute;left:0;width:100%;display:block;font-weight:400;font-size:40px;line-height:36px;letter-spacing:6px;padding-left:6px}
  .brand__line--one{top:98px}
  .brand__line--two{top:134px}
  .brand__tag{position:absolute;left:0;width:100%;top:174px;font-size:16px;line-height:18px;letter-spacing:3.5px;padding-left:3px;font-weight:400}

  .value{position:absolute;white-space:nowrap}
  .value h3{font-family:"Poppins",Arial,sans-serif;font-size:15px;font-weight:600;color:var(--teal-deep);line-height:18px;letter-spacing:.2px}
  .value p{font-size:12.5px;color:var(--ink);line-height:17px}
  .value--left{left:228px}
  .value--left h3::before{content:"";display:inline-block;width:6px;height:6px;border-radius:50%;background:var(--bullet);margin-right:6px;vertical-align:middle;position:relative;top:-2px}
  .value--left p{padding-left:12px}
  .value--right{right:198px;text-align:right}
  .value--right h3::before{content:"";display:inline-block;width:6px;height:6px;border-radius:50%;background:var(--bullet);margin-right:6px;vertical-align:middle;position:relative;top:-2px}

  .service{position:absolute;color:var(--white);white-space:nowrap}
  .service h2{position:absolute;font-family:"Poppins",Arial,sans-serif;font-size:23px;font-weight:500;letter-spacing:.5px;line-height:26px}
  .service p{position:absolute;font-size:12.5px;line-height:16px}
  .service--tax h2{left:406px;top:747px}
  .service--tax p{right:605px;top:784px;text-align:right}
  .service--acct h2{left:679px;top:747px}
  .service--acct p{left:643px;top:784px}

  .pillar{
    position:absolute;top:1042px;height:56px;border-radius:28px;
    background:var(--yellow);border:5px solid var(--white);
    box-shadow:0 3px 6px rgba(0,0,0,.12);
    display:flex;align-items:center;justify-content:center;
    font-family:"Poppins",Arial,sans-serif;font-size:23px;font-weight:500;color:var(--teal-deep);letter-spacing:.4px;
  }
  .pillar--trust{left:222px;width:256px}
  .pillar--transparency{left:486px;width:262px}
  .pillar--dependability{left:754px;width:254px}

  .label{font-family:"Poppins",Arial,sans-serif;font-weight:500;font-size:13px;letter-spacing:.3px}
  .label--dark{fill:var(--teal-deep)}
  .label--light{fill:var(--white)}
  .label--core{font-weight:300;font-size:33px;fill:var(--teal-deep);letter-spacing:1px}
  .icon{fill:none;stroke:var(--white);stroke-width:2.4;stroke-linecap:round;stroke-linejoin:round}
  .icon--dark{stroke:var(--teal-deep)}
</style>
</head>
<body>
<main class="poster">
  <div class="band band--top"></div>
  <div class="band band--bottom"></div>
</main>

<svg class="graphic" viewBox="0 0 1200 1200" aria-hidden="true">
  <defs>
    <clipPath id="poster-area"><rect x="204" y="74" width="822" height="1066"/></clipPath>
    <filter id="soft-shadow" x="-20%" y="-20%" width="140%" height="140%">
      <feDropShadow dx="0" dy="3" stdDeviation="5" flood-color="#000" flood-opacity=".14"/>
    </filter>
  </defs>

  <g clip-path="url(#poster-area)">
    <!-- header arc -->
    <circle cx="615" cy="-88" r="314" fill="var(--yellow-ring)" filter="url(#soft-shadow)"/>
    <circle cx="615" cy="-88" r="307" fill="var(--white)"/>

    <!-- main disc -->
    <circle cx="615" cy="632" r="316" fill="var(--white)" filter="url(#soft-shadow)"/>
    <circle cx="615" cy="632" r="304" fill="var(--yellow-ring)"/>
    <circle cx="615" cy="632" r="297" fill="var(--white)"/>
    <circle cx="615" cy="632" r="290" fill="var(--teal)"/>

    <!-- stem -->
    <rect x="602" y="620" width="26" height="390" fill="var(--white)"/>

    <!-- core values wheel -->
    <circle cx="615" cy="522" r="192" fill="var(--white)" filter="url(#soft-shadow)"/>
    <g stroke="var(--white)" stroke-width="8" stroke-linejoin="round">
      <!-- empower: 178° to 265° -->
      <path d="M615 522 L432.1 528.4 A183 183 0 0 1 599.1 339.7 Z" fill="var(--teal-light)"/>
      <!-- client focused: 265° to 30° -->
      <path d="M615 522 L599.1 339.7 A183 183 0 0 1 773.5 613.5 Z" fill="var(--teal-mid)"/>
      <!-- rectitude: 30° to 103° -->
      <path d="M615 522 L773.5 613.5 A183 183 0 0 1 573.8 700.3 Z" fill="var(--teal-light)"/>
      <!-- relentless: 103° to 178° -->
      <path d="M615 522 L573.8 700.3 A183 183 0 0 1 432.1 528.4 Z" fill="var(--teal-mid)"/>
    </g>
    <circle cx="615" cy="522" r="80" fill="var(--white)"/>
    <text class="label--core" x="615" y="518" text-anchor="middle">CORE</text>
    <text class="label--core" x="615" y="551" text-anchor="middle">VALUES</text>
    <rect x="570" y="556" width="92" height="4" fill="var(--yellow-ring)"/>

    <!-- empower -->
    <path class="icon icon--dark" d="M570 382 l6 13 14 2 -10 10 2 14 -12 -7 -12 7 2 -14 -10 -10 14 -2z"/>
    <text class="label label--dark" x="532" y="456" text-anchor="middle">EMPOWER</text>

    <!-- client focused -->
    <g class="icon">
      <circle cx="720" cy="424" r="7"/>
      <path d="M708 446 q12 -16 24 0"/>
      <path d="M696 432 q-6 18 10 26 l6 6 M744 432 q6 18 -10 26 l-6 6"/>
    </g>
    <text class="label label--light" x="756" y="502" text-anchor="middle">CLIENT</text>
    <text class="label label--light" x="756" y="518" text-anchor="middle">FOCUSED</text>

    <!-- relentless -->
    <g class="icon">
      <rect x="470" y="566" width="28" height="22" rx="5"/>
      <path d="M477 566 v10 M484 566 v10 M491 566 v10 M474 588 v10 h20 v-10"/>
      <path d="M474 556 l-3 -5 M484 554 v-7 M494 556 l3 -5"/>
    </g>
    <text class="label label--light" x="523" y="621" text-anchor="middle">RELENTLESS</text>

    <!-- rectitude -->
    <g class="icon icon--dark">
      <circle cx="690" cy="624" r="17"/>
      <path d="M681 624 l7 7 18 -20"/>
    </g>
    <text class="label label--dark" x="662" y="672" text-anchor="middle">RECTITUDE</text>

    <!-- tax icon -->
    <g class="icon">
      <path d="M370 664 h32 l10 10 v54 h-42 z"/>
      <path d="M377 694 h20 M377 704 h26 M377 714 h26"/>
      <text x="377" y="686" fill="var(--white)" stroke="none" font-family="Poppins,Arial,sans-serif" font-size="12" font-weight="500">TAX</text>
    </g>

    <!-- accounting icon -->
    <g class="icon">
      <rect x="802" y="664" width="32" height="44" rx="4"/>
      <rect x="808" y="670" width="20" height="9"/>
      <path d="M809 687 h2 M817 687 h2 M825 687 h2 M809 695 h2 M817 695 h2 M825 695 h2"/>
      <path d="M834 680 h22 l8 8 v42 h-30"/>
      <path d="M842 694 h14 M842 704 h14"/>
      <circle cx="830" cy="716" r="10"/>
      <path d="M872 702 l-14 24"/>
    </g>

    <!-- pillar icon circles -->
    <circle cx="354" cy="1014" r="50" fill="var(--white)"/>
    <circle cx="354" cy="1014" r="44" fill="var(--teal)"/>
    <circle cx="617" cy="1012" r="50" fill="var(--white)"/>
    <circle cx="617" cy="1012" r="44" fill="var(--teal)"/>
    <circle cx="878" cy="1012" r="50" fill="var(--white)"/>
    <circle cx="878" cy="1012" r="44" fill="var(--teal)"/>

    <g class="icon">
      <path d="M330 1004 l10 -8 14 6 14 -6 10 8"/>
      <path d="M344 1010 l10 10 M350 1006 l10 10 M356 1002 l10 10"/>
    </g>
    <g class="icon">
      <path d="M595 1008 q22 -22 44 0 q-22 22 -44 0z"/>
      <circle cx="617" cy="1008" r="6"/>
      <path d="M617 986 v-6 M603 990 l-3 -5 M631 990 l3 -5"/>
    </g>
    <g class="icon">
      <path d="M862 1024 l-6 -20 10 -10 14 8 M894 994 l6 20 -10 10 -14 -8"/>
      <path d="M868 998 l20 20"/>
    </g>
  </g>
</svg>

<header class="brand">
  <span class="brand__line brand__line--one">MAPLE</span>
  <span class="brand__line brand__line--two">FINCH</span>
  <span class="brand__tag">ADVISORY</span>
</header>

<section class="value value--left" style="top:226px">
  <h3>EMPOWER</h3>
  <p>We are dedicated, appreciative and respectful<br>of people’s time and purpose.</p>
</section>
<section class="value value--left" style="top:283px">
  <h3>RELENTLESS</h3>
  <p>We believe that the longer we try<br>to do our best, the better we become.</p>
</section>
<section class="value value--right" style="top:220px">
  <h3>CLIENT FOCUSED</h3>
  <p>We provide a personal service that goes<br>above the standards of professional care.</p>
</section>
<section class="value value--right" style="top:277px">
  <h3>RECTITUDE</h3>
  <p>We know the difference between what<br>we have the right to do and what<br>the right thing to do is.</p>
</section>

<section class="service service--tax">
  <h2>TAX</h2>
  <p>Maple Finch provides all clients<br>with a trusted tax advisor who<br>provides accuracy in all filings<br>&amp; ensures your compliance<br>with all government<br>agencies.</p>
</section>
<section class="service service--acct">
  <h2>ACCOUNTING</h2>
  <p>Maple Finch provides all<br>business owners with the<br>financial visibility needed<br>to foster growth and<br>facilitate goals.</p>
</section>

<div class="pillar pillar--trust">TRUST</div>
<div class="pillar pillar--transparency">TRANSPARENCY</div>
<div class="pillar pillar--dependability">DEPENDABILITY</div>
</body>
</html>
```